Tui Netlink Website

We're looking for a basic website and order form for our stripped down ISP, Tui Netlink.

The front page should be basic with our two plan options - we're open to pretty much any design, but one possibility is an image of New Zealand with two clouds above it (similar to the quick mockup attached).

Clicking on one of the plans will then take the user to a basic order form.

We will also need a contact, about, and support page.

Industry/Entity Type

Isp

```html
<!DOCTYPE html>
<html lang="en">
<head>
<meta charset="utf-8">
<title>Tui Netlink – Contact</title>
<link rel="stylesheet" href="https://fonts.googleapis.com/css2?family=Didact+Gothic&family=Open+Sans:wght@400;700&family=Arimo:wght@400;700&display=swap">
<style>
  :root {
    --bg-green: #359a1c;
    --bg-teal: #0f9d70;
    --sweep: rgba(255,255,255,0.22);
    --button-green: #2f9a1a;
    --panel: rgba(12,100,62,0.72);
    --field: #0b5e37;
    --field-text: #93d3a4;
    --info-text: #c6efd2;
    --submit-bg: #d0e8dc;
    --submit-text: #0b5e37;
    --heading-green: #3a9a1a;
    --white: #ffffff;
  }
  * { box-sizing: border-box; margin: 0; padding: 0; }
  html, body { width: 1200px; height: 889px; overflow: hidden; }
  body {
    position: relative;
    font-family: "Arimo", Arial, sans-serif;
    background: linear-gradient(20deg, var(--bg-green) 0%, #25a03f 50%, var(--bg-teal) 100%);
    color: var(--white);
  }
  .backdrop { position: absolute; inset: 0; }
  .account-bar {
    position: absolute; left: 809px; top: 40px; width: 266px; height: 35px;
    background: var(--button-green); border-radius: 4px;
    display: flex; align-items: center; font-size: 14px;
  }
  .account-bar a { color: var(--white); text-decoration: none; flex: 1; text-align: center; }
  .account-bar .divider { width: 1px; height: 18px; background: rgba(255,255,255,0.8); }
  .brand { position: absolute; left: 145px; top: 82px; }
  .brand-name { font-family: "Open Sans", sans-serif; font-weight: 700; font-size: 35px; line-height: 44px; letter-spacing: -0.5px; }
  .brand-tagline { font-family: "Didact Gothic", sans-serif; font-size: 12.5px; letter-spacing: 1.1px; margin-left: 8px; margin-top: -1px; }
  .main-nav { position: absolute; right: 125px; top: 124px; display: flex; gap: 22px; }
  .main-nav a { font-family: "Didact Gothic", sans-serif; font-size: 14px; color: var(--white); text-decoration: none; letter-spacing: 0.3px; }
  .country-art { position: absolute; left: 820px; top: 175px; width: 205px; height: 370px; }
  .page-title { position: absolute; left: 138px; top: 210px; width: 352px; height: 200px; z-index: 2; }
  .page-title h1 {
    position: absolute; left: 48px; top: 78px;
    font-family: "Didact Gothic", sans-serif; font-weight: 400;
    font-size: 58px; color: var(--heading-green); letter-spacing: -1px; line-height: 64px;
  }
  .contact-panel { position: absolute; left: 125px; top: 370px; width: 960px; height: 461px; background: var(--panel); border-radius: 3px; }
  .contact-form { position: absolute; left: 48px; top: 70px; width: 361px; }
  .field {
    display: block; width: 100%; height: 40px; margin-bottom: 2px; padding: 0 20px;
    background: var(--field); border: none; border-radius: 3px;
    font-family: "Arimo", Arial, sans-serif; font-size: 14px; color: var(--field-text);
  }
  .field::placeholder { color: var(--field-text); }
  textarea.field { height: 129px; padding-top: 12px; resize: none; }
  .submit {
    margin-top: 17px; margin-left: 1px; width: 154px; height: 41px; border: none; border-radius: 4px;
    background: var(--submit-bg); color: var(--submit-text); font-family: "Arimo", Arial, sans-serif; font-size: 14px;
  }
  .contact-info { position: absolute; left: 460px; top: 68px; color: var(--info-text); }
  .contact-info h2 { font-family: "Arimo", Arial, sans-serif; font-weight: 700; font-size: 22px; line-height: 28px; margin-bottom: 6px; color: #d8f5e0; }
  .contact-info p { font-size: 14px; line-height: 17px; }
  .location-map { position: absolute; left: 459px; top: 166px; width: 362px; height: 203px;
    background: linear-gradient(135deg, #ece6d6 0%, #f1e7c9 45%, #f4d680 70%, #dfe9d2 100%); }
  .site-footer { position: absolute; left: 131px; right: 116px; top: 856px; display: flex; justify-content: space-between; font-size: 12px; }
  .footer-nav { display: flex; gap: 10px; }
  .footer-nav a { color: var(--white); text-decoration: none; }
</style>
</head>
<body>
  <svg class="backdrop" width="1200" height="889" viewBox="0 0 1200 889" aria-hidden="true">
    <path d="M604 0 C700 150 860 330 1000 450 C1080 520 1150 570 1200 600 L1200 0 Z" fill="var(--sweep)"/>
  </svg>

  <nav class="account-bar">
    <a href="#">My Account</a><span class="divider"></span><a href="#">Order Now</a>
  </nav>

  <header class="brand">
    <div class="brand-name">tuinetlink</div>
    <div class="brand-tagline">PURE BROADBAND. PURE SPEED. NO LIMITS</div>
  </header>

  <nav class="main-nav">
    <a href="#">HOME</a><a href="#">PROMOS</a><a href="#">PRICING</a><a href="#">SUPPORT</a><a href="#">CONTACT</a>
  </nav>

  <svg class="country-art" viewBox="0 0 205 370" role="img" aria-label="Silhouette of New Zealand's North Island">
    <defs>
      <radialGradient id="islandGlow" cx="50%" cy="45%" r="55%">
        <stop offset="0%" stop-color="#ffffff" stop-opacity="0.55"/>
        <stop offset="100%" stop-color="#ffffff" stop-opacity="0"/>
      </radialGradient>
    </defs>
    <rect width="205" height="370" fill="url(#islandGlow)"/>
  </svg>

  <div class="page-title">
    <svg width="352" height="200" viewBox="0 0 352 200" aria-hidden="true">
      <g fill="var(--white)">
        <circle cx="100" cy="85" r="72"/>
        <circle cx="205" cy="68" r="55"/>
        <circle cx="275" cy="105" r="70"/>
        <circle cx="75" cy="125" r="68"/>
        <circle cx="165" cy="140" r="55"/>
        <circle cx="255" cy="150" r="40"/>
      </g>
    </svg>
    <h1>CONTACT</h1>
  </div>

  <main class="contact-panel">
    <form class="contact-form">
      <input class="field" type="text" placeholder="Name">
      <input class="field" type="email" placeholder="Email">
      <input class="field" type="text" placeholder="Username/account number">
      <input class="field" type="text" placeholder="Subject">
      <textarea class="field" placeholder="Message"></textarea>
      <button class="submit" type="submit">Submit</button>
    </form>

    <section class="contact-info">
      <h2>tuinetlink</h2>
      <p>PO Box 4521, Harbour Lane, Auckland 1010</p>
      <p>Phone: +1 555 014 2290</p>
      <p>Email: hello@tuinetlink.co.nz</p>
    </section>
    <div class="location-map" role="img" aria-label="Street map of central Auckland with office location pin"></div>
  </main>

  <footer class="site-footer">
    <nav class="footer-nav">
      <a href="#">home</a><a href="#">products</a><a href="#">promos</a><a href="#">pricing</a><a href="#">support</a><a href="#">contact</a>
    </nav>
    <p>Questions? Call our 24/7 hotline <strong>5021 4470</strong> or visit one of our retail outlets.</p>
  </footer>
</body>
</html>
```